QB-Electronics advertising flag and billboard design

I need a design for advertising flag and a design for billboard.
Information can be obtained from https://qb-elektronik-example.de.
Target Market(s)
IT service for companies
Requirements
Must have
- Logo, contact information and services

```html
<!DOCTYPE html>
<html lang="en">
<head>
<meta charset="utf-8">
<title>QB-Electronics Billboard</title>
<link href="https://fonts.googleapis.com/css2?family=Open+Sans:wght@600;700;800&display=swap" rel="stylesheet">
<style>
  :root {
    --page-bg: #e9ebee;
    --panel-dark: #3a3a3d;
    --panel-border: #ffffff;
    --text-light: #ffffff;
    --accent-blue: #4a64c8;
    --photo-white: #f4f4f3;
    --photo-grey: #d9d8d6;
    --photo-skin: #e6c2aa;
    --photo-shirt: #f7f6f4;
    --photo-hair: #c8612b;
    --photo-device: #2c2c30;
  }
  html, body {
    margin: 0;
    padding: 0;
    width: 1200px;
    height: 801px;
    overflow: hidden;
    background: var(--page-bg);
  }
  .billboard {
    position: absolute;
    left: 0;
    top: 100px;
    width: 1200px;
    height: 600px;
    overflow: hidden;
    font-family: "Open Sans", sans-serif;
  }
  .billboard__photo {
    position: absolute;
    inset: 0;
    background:
      linear-gradient(90deg,
        transparent 0%, transparent 78%,
        rgba(200, 97, 43, 0.35) 82%, rgba(200, 97, 43, 0.85) 86%,
        rgba(200, 97, 43, 0.85) 91%, rgba(200, 97, 43, 0.3) 94%,
        transparent 97%),
      linear-gradient(180deg,
        transparent 0%, transparent 62%,
        rgba(44, 44, 48, 0.0) 62%) ,
      linear-gradient(90deg,
        var(--photo-white) 0%, var(--photo-grey) 22%,
        var(--photo-white) 34%, var(--photo-skin) 52%,
        var(--photo-shirt) 62%, var(--photo-skin) 72%,
        var(--photo-shirt) 80%, var(--photo-shirt) 100%);
  }
  .billboard__photo::after {
    content: "";
    position: absolute;
    left: 0;
    top: 0;
    width: 100%;
    height: 100%;
    background: linear-gradient(200deg,
      transparent 0%, transparent 58%,
      rgba(44, 44, 48, 0.55) 72%, rgba(44, 44, 48, 0.85) 85%);
    -webkit-mask: linear-gradient(90deg, #000 0%, #000 22%, transparent 34%);
    mask: linear-gradient(90deg, #000 0%, #000 22%, transparent 34%);
  }
  .brand-panel {
    position: absolute;
    left: 181px;
    top: 188px;
    width: 812px;
    height: 198px;
    box-sizing: border-box;
    background: var(--panel-dark);
    border: 2px solid var(--panel-border);
    border-radius: 14px;
    color: var(--text-light);
    text-align: center;
    display: flex;
    flex-direction: column;
    justify-content: center;
    gap: 4px;
    z-index: 1;
  }
  .brand-panel__name {
    font-size: 32px;
    font-weight: 800;
    letter-spacing: 3px;
    text-transform: uppercase;
    line-height: 1.1;
  }
  .brand-panel__tagline {
    font-size: 50px;
    font-weight: 700;
    line-height: 1.15;
  }
  .brand-panel__tagline-accent {
    color: var(--accent-blue);
  }
  .brand-panel__url {
    font-size: 27px;
    font-weight: 600;
    line-height: 1.2;
    margin-top: 8px;
  }
</style>
</head>
<body>
  <section class="billboard">
    <div class="billboard__photo" role="img" aria-label="Photo of two smiling colleagues working together at a laptop in a bright office"></div>
    <div class="brand-panel">
      <div class="brand-panel__name">QB-Electronics</div>
      <div class="brand-panel__tagline">Your partner for <span class="brand-panel__tagline-accent">IT-Services</span></div>
      <div class="brand-panel__url">https://qb-elektronik-example.de</div>
    </div>
  </section>
</body>
</html>
```